BOLD & MINIMALIST DESIGN NEEDED

We want a very bold but minimalistic business card design that is impactful and utilizes both sides of the business card. Our current logo is included for your use.

We want bold fonts and good use of negative space. We don't want the logo to overpower the design.

Target Market(s)

Professionals who are building new commercial buildings.

Industry/Entity Type

Construction

Contact Information for Business Card

Name, Title, email, office phone, cell phone, website

Font styles to use
Serif
Sans Serif

Requirements
Must have
• Bold design!

```html
<!DOCTYPE html>
<html lang="en">
<head>
<meta charset="utf-8">
<title>Ridgeline Design + Build — Business Card</title>
<link rel="stylesheet" href="https://fonts.googleapis.com/css2?family=Montserrat:wght@400;500;600;800&display=swap">
<style>
  :root {
    --bg: #e9e9e9;
    --paper: #ffffff;
    --ink: #111111;
    --green: #7cc242;
    --dark: #1c1c1c;
  }
  * { box-sizing: border-box; margin: 0; padding: 0; }
  html, body {
    width: 1200px; height: 1200px; overflow: hidden;
    background: var(--bg);
    font-family: "Montserrat", Arial, sans-serif;
  }
  .canvas { position: relative; width: 1200px; height: 1200px; }
  .card {
    position: absolute; left: 150px; width: 900px; height: 514px;
    border-radius: 30px; overflow: hidden;
    box-shadow: 0 10px 30px rgba(0,0,0,.18);
  }
  .card--front { top: 52px; background: var(--paper); }
  .card--back { top: 634px; background: var(--dark); border-bottom: 5px solid var(--green); }

  .person { position: absolute; left: 90px; top: 150px; }
  .person__name { color: var(--green); font-weight: 600; font-size: 40px; letter-spacing: 1px; line-height: 1.1; }
  .person__title { color: var(--ink); font-weight: 500; font-size: 30px; line-height: 1.2; margin-bottom: 18px; }
  .contact { list-style: none; }
  .contact__item {
    display: flex; align-items: center; gap: 16px;
    font-size: 26px; color: var(--ink); line-height: 1; margin-bottom: 14px;
  }
  .contact__icon { width: 28px; height: 28px; flex: none; }

  .brand { position: absolute; right: 70px; top: 150px; text-align: center; color: var(--ink); font-weight: 800; }
  .brand__name { font-size: 62px; letter-spacing: 1px; line-height: 1; }
  .brand__sub { font-size: 22px; letter-spacing: 8px; margin-top: 10px; }

  .band { position: absolute; bottom: 0; }
  .band--green { left: 0; width: 580px; height: 24px; background: var(--green); }
  .band--black { left: 596px; right: 0; height: 54px; background: var(--ink); }

  .back-brand {
    position: absolute; left: 50%; top: 50%; transform: translate(-50%, -50%);
    color: var(--paper); font-weight: 800; text-align: center; white-space: nowrap;
  }
  .back-brand__name { font-size: 54px; line-height: 1; }
  .back-brand__sub { font-size: 19px; letter-spacing: 7px; margin-top: 8px; }
</style>
</head>
<body>
<main class="canvas">

  <section class="card card--front" aria-label="Card front">
    <div class="person">
      <p class="person__name">FULL NAME</p>
      <p class="person__title">TITLE</p>
      <ul class="contact">
        <li class="contact__item">
          <svg class="contact__icon" viewBox="0 0 28 28" fill="none" stroke="var(--green)" stroke-width="2"><rect x="8" y="2" width="12" height="24" rx="2"/><line x1="12" y1="22" x2="16" y2="22"/></svg>
          (000) 000 0000
        </li>
        <li class="contact__item">
          <svg class="contact__icon" viewBox="0 0 28 28" fill="var(--green)"><path d="M7 3l5 5-3 3c1.5 3.5 4.5 6.5 8 8l3-3 5 5-3 4C11 24 4 17 3 7z"/></svg>
          (000) 000 0000
        </li>
        <li class="contact__item">
          <svg class="contact__icon" viewBox="0 0 28 28" fill="none" stroke="var(--green)" stroke-width="1.8"><circle cx="14" cy="14" r="11"/><ellipse cx="14" cy="14" rx="5" ry="11"/><line x1="3" y1="14" x2="25" y2="14"/><line x1="5" y1="8" x2="23" y2="8"/><line x1="5" y1="20" x2="23" y2="20"/></svg>
          www.company.com
        </li>
        <li class="contact__item">
          <svg class="contact__icon" viewBox="0 0 28 28" fill="none" stroke="var(--green)" stroke-width="2"><rect x="2" y="6" width="24" height="16"/><polyline points="2,6 14,16 26,6"/></svg>
          email@company.com
        </li>
      </ul>
    </div>

    <div class="brand">
      <p class="brand__name">RIDGELINE</p>
      <p class="brand__sub">DESIGN + BUILD</p>
    </div>

    <div class="band band--green"></div>
    <div class="band band--black"></div>
  </section>

  <section class="card card--back" aria-label="Card back">
    <div class="back-brand">
      <p class="back-brand__name">RIDGELINE</p>
      <p class="back-brand__sub">DESIGN + BUILD</p>
    </div>
  </section>

</main>
</body>
</html>
```